Redesign of an educational Eye website for Medical Students and Healthcare professionals

www.corvantisportal.com is an educational resource, illustrated using high quality 3D animations, for undergraduate medical students and healthcare professionals to learn about the anatomy of the human eye and associated common eye disorders.

The website was originally developed (using a Joomla template) a couple of years ago and we now want to update the brand and design of the site. Example content and animations can be found at https://www.corvantisportal.com/overview or https://www.corvantisportal.com/ocular-anatomy/orbital-anatomy

We would like a new logo and home page design (to include new colour palette, fonts and updated overall design).

The attached PowerPoint contains an example layout of the revised components we want to appear on the new Home page. We plan to have a hero panel at the top of page playing a short video of some of the animations. Similar to how this site works (www.zembri.uk.com).

We want the new site to feel Professional, Modern and Clean and simple.

Target Market(s)

Undergraduate medical students and Healthcare Professionals

Industry/Entity Type

Medical

Logo Text

Corvantis Portal

Number of Pages Required

1 page

Font styles to use
Sans Serif

Colors

Designer to choose colors to be used in the design.

```html
<!DOCTYPE html>
<html lang="en">
<head>
<meta charset="utf-8">
<title>Corvantis Portal — Learn Faster and Smarter</title>
<link rel="stylesheet" href="https://fonts.googleapis.com/css2?family=Montserrat:ital,wght@0,400;0,600;0,700;0,800;1,700;1,800&family=Open+Sans:ital,wght@0,400;0,600;0,700;1,400&display=swap">
<style>
:root{
  --navy:#1f4a62;
  --navy-deep:#183c50;
  --blue:#29a8e0;
  --blue-soft:#4dbbe9;
  --teal:#5ccdc3;
  --teal-deep:#3fb6ac;
  --grey-bg:#f2f2f2;
  --text:#6b7378;
  --white:#ffffff;
  --head:"Montserrat",sans-serif;
  --body:"Open Sans",sans-serif;
}
*{box-sizing:border-box;margin:0;padding:0}
html,body{width:1200px;height:5056px;overflow:hidden}
body{font-family:var(--body);color:var(--text);background:var(--white);position:relative}
section,header,footer{position:relative;width:1200px;overflow:hidden}
.abs{position:absolute}
.spaced-title{font-family:var(--head);font-weight:600;letter-spacing:9px;text-transform:uppercase;color:var(--blue);font-size:20px;text-align:center}
.title-rule{width:60px;height:2px;background:var(--blue);margin:14px auto 0;opacity:.5}
.btn{display:inline-block;font-family:var(--head);font-weight:700;font-size:11px;letter-spacing:1px;text-transform:uppercase;color:var(--white);background:var(--blue);padding:13px 22px}
.photo{position:absolute}

/* nav */
.site-nav{position:absolute;top:0;left:0;width:1200px;height:66px;z-index:5;background:rgba(255,255,255,.96)}
.brand{position:absolute;left:232px;top:17px;display:flex;align-items:center;gap:10px}
.brand-dot{width:32px;height:32px;border-radius:50%;background:var(--blue)}
.brand-name{font-family:var(--head);font-weight:700;font-size:17px;color:var(--blue)}
.nav-links{position:absolute;left:550px;top:0;height:66px;display:flex;align-items:center;gap:38px;font-family:var(--head);font-size:10px;font-weight:600;letter-spacing:1px;color:#8a9296}
.nav-links .active{color:var(--blue)}
.nav-login{position:absolute;left:905px;top:0;width:58px;height:66px;background:var(--blue);color:var(--white);font-family:var(--head);font-size:10px;font-weight:700;display:flex;align-items:center;justify-content:center;letter-spacing:1px}

/* hero */
.hero{height:674px}
.hero-photo{inset:0;background:linear-gradient(100deg,#2f6581 0%,#244f67 45%,#2b5c75 70%,#1e455b 100%)}
.hero-shade{position:absolute;inset:0;background:rgba(24,60,80,.55)}
.hero-title{position:absolute;top:258px;width:100%;text-align:center;font-family:var(--head);font-weight:800;font-size:46px;color:var(--white);letter-spacing:1px}
.hero-text{position:absolute;top:330px;left:330px;width:540px;text-align:center;color:#dbe8ef;font-size:13px;line-height:20px}
.hero-actions{position:absolute;top:418px;width:100%;display:flex;justify-content:center;gap:46px}
.hero-dots{position:absolute;top:632px;width:100%;display:flex;justify-content:center;gap:7px}
.hero-dots span{width:8px;height:8px;border-radius:50%;border:1px solid #9ec3d6}
.hero-dots .on{background:#9ec3d6}

/* trusted */
.trusted{height:337px;background:var(--white)}
.trusted .spaced-title{position:absolute;top:86px;width:100%}
.trusted .title-rule{position:absolute;top:112px;left:570px}
.badges{position:absolute;top:170px;left:250px;width:700px;display:flex;justify-content:space-between;align-items:center}
.badge{width:130px;height:82px;display:flex;flex-direction:column;align-items:center;gap:8px}
.badge-shape{width:40px;height:46px;border-radius:6px 6px 20px 20px;background:#c9cdd0}
.badge-bar{width:110px;height:10px;background:#dcdfe1}
.badge-sep{width:1px;height:70px;background:#d9dcde}

/* why */
.why{height:903px;background:var(--grey-bg)}
.why .spaced-title{position:absolute;top:70px;width:100%}
.why .title-rule{position:absolute;top:96px;left:570px}
.frame{position:absolute;border:7px solid var(--teal)}
.frame.blue{border-color:var(--blue)}
.feature-heading{font-family:var(--head);font-weight:600;font-size:18px;letter-spacing:8px;color:#3e4a50;text-transform:uppercase}
.feature-copy{font-size:10.5px;line-height:17px;color:#7c8489;margin-top:18px}
.feature-list{list-style:none;margin-top:4px;font-size:10.5px;line-height:17px;color:#7c8489}
.feature-list li::before{content:"";display:inline-block;width:6px;height:6px;background:var(--blue);margin-right:8px;vertical-align:1px}

/* modules */
.modules{height:553px}
.modules-bg{inset:0;background:linear-gradient(90deg,#2aa8df 0%,#2aa5dc 55%,#4db3de 80%,#3aa6d6 100%)}
.modules .spaced-title{position:absolute;top:60px;width:100%;color:var(--white)}
.modules .title-rule{position:absolute;top:86px;left:570px;background:var(--white)}
.module{position:absolute;top:160px;width:200px;text-align:center}
.module-ring{width:164px;height:164px;border-radius:50%;border:7px solid var(--white);background:var(--teal);margin:0 auto;display:flex;align-items:center;justify-content:center}
.module-name{font-family:var(--head);font-weight:700;font-size:12px;letter-spacing:1px;color:var(--white);margin-top:26px;text-transform:uppercase}
.module-text{font-size:10px;line-height:15px;color:#e3f4fb;margin-top:6px;padding:0 18px}
.module .btn{background:var(--teal-deep);margin-top:22px;padding:11px 22px;font-size:10px}

/* team */
.team{height:539px;background:var(--white)}
.team .spaced-title{position:absolute;top:58px;width:100%}
.team .title-rule{position:absolute;top:84px;left:570px}
.member{position:absolute;top:138px;width:245px;height:340px}
.member-photo{position:absolute;inset:0;background:linear-gradient(160deg,#eef0f1 0%,#d8dde0 100%)}
.member-bar{position:absolute;left:0;bottom:0;width:100%;height:66px;background:rgba(50,58,64,.85);text-align:center;padding-top:16px}
.member-name{font-family:var(--head);font-weight:700;font-size:11px;letter-spacing:3px;color:var(--white);text-transform:uppercase}
.member-role{font-size:9px;color:#c4cacd;margin-top:4px}
.member.featured .member-photo{background:var(--teal)}
.member.featured .featured-inner{position:absolute;inset:0;text-align:center;padding:46px 26px 0}
.featured-inner .member-name{font-size:12px}
.featured-inner .member-role{color:#eafaf8}
.featured-inner p{font-size:10px;line-height:16px;color:#f2fcfb;margin-top:20px}
.featured-inner .btn{margin-top:26px;font-size:10px}

/* testimonials */
.testimonials{height:371px;background:var(--navy)}
.testimonials .spaced-title{position:absolute;top:56px;width:100%;color:var(--white);letter-spacing:3px;font-size:18px}
.testimonials .title-rule{position:absolute;top:82px;left:570px;background:var(--white);opacity:.4}
.avatar{position:absolute;left:298px;top:150px;width:60px;height:60px;border-radius:50%;background:linear-gradient(#c7ccd0,#9ba3a8)}
.quote-author{position:absolute;left:296px;top:226px;font-family:var(--head);font-weight:700;font-size:11px;letter-spacing:2px;color:var(--white)}
.quote-role{position:absolute;left:296px;top:244px;font-size:9px;color:#a8bcc8}
.quote-lead{position:absolute;left:420px;top:150px;width:500px;font-size:10.5px;font-weight:700;color:var(--white)}
.quote-body{position:absolute;left:420px;top:188px;width:500px;font-size:10.5px;line-height:17px;font-style:italic;color:#c3d3dc}
.arrow{position:absolute;top:165px}
.t-dots{position:absolute;left:296px;top:278px;display:flex;gap:6px}
.t-dots span{width:7px;height:7px;border-radius:50%;border:1px solid #9fb6c3}
.t-dots .on{background:#9fb6c3}

/* trial */
.trial{height:499px}
.trial-bg{inset:0;background:linear-gradient(90deg,#52c7bd 0%,#5ccdc3 50%,#6fd1c8 100%)}
.trial-circle{position:absolute;top:86px;width:150px;height:150px;border-radius:50%;border:5px solid var(--white)}
.trial-title{position:absolute;top:260px;width:100%;text-align:center;font-family:var(--head);font-weight:800;font-style:italic;font-size:29px;line-height:36px;color:var(--white)}
.trial-note{position:absolute;top:336px;width:100%;text-align:center;font-family:var(--head);font-weight:700;font-style:italic;font-size:13px;color:#e8faf8}
.trial .btn{position:absolute;top:388px;left:520px;width:160px;text-align:center;background:transparent;border:2px solid var(--navy);color:var(--navy);letter-spacing:3px}

/* charity */
.charity{height:243px;background:var(--blue)}
.charity h2{position:absolute;top:62px;width:100%;text-align:center;font-family:var(--head);font-weight:700;font-size:26px;color:var(--white)}
.charity p{position:absolute;top:118px;left:330px;width:540px;text-align:center;font-style:italic;font-weight:600;font-size:13px;line-height:21px;color:#e6f5fc}

/* contact */
.contact{height:599px;background:var(--white)}
.contact-photo{left:0;top:0;width:600px;height:599px;background:linear-gradient(110deg,#e8ecee 0%,#d6dde1 60%,#c3ccd1 100%)}
.contact-panel{position:absolute;left:600px;top:0;width:600px;height:599px;background:#fafafa}
.contact-kicker{position:absolute;left:608px;top:94px;font-family:var(--head);font-size:10px;letter-spacing:5px;color:#9aa2a6}
.contact-title{position:absolute;left:608px;top:116px;font-family:var(--head);font-weight:600;font-size:20px;letter-spacing:9px;color:var(--blue)}
.contact-intro{position:absolute;left:608px;top:164px;width:300px;font-size:10px;line-height:16px;color:#8a9296}
.field{position:absolute;height:30px;border:1px solid #dfe3e5;background:var(--white);font-size:9px;color:#a4abaf;padding:9px 10px}
.field.focus{border-color:var(--blue)}
.contact .btn{position:absolute;left:842px;top:480px;padding:11px 18px;font-size:10px}

/* footer */
.site-footer{height:297px;background:var(--navy)}
.site-footer .brand{left:236px;top:54px}
.site-footer .brand-name{color:var(--white)}
.community{position:absolute;left:236px;top:120px;font-family:var(--head);font-weight:700;font-size:10px;letter-spacing:3px;color:var(--white)}
.socials{position:absolute;left:236px;top:146px;display:flex;gap:9px}
.socials span{width:24px;height:24px;border-radius:50%;background:var(--blue)}
.foot-col{position:absolute;top:60px}
.foot-col h4{font-family:var(--head);font-weight:700;font-size:10px;letter-spacing:3px;color:var(--white)}
.foot-col ul{list-style:none;margin-top:16px;font-size:10px;line-height:18px;color:#b9cad4}
.foot-col p{margin-top:16px;font-size:9.5px;line-height:15px;color:#b9cad4;width:190px}
.subscribe{display:flex;margin-top:14px;width:180px;height:28px;border:1px solid #6e8c9d}
.subscribe span{flex:1;font-size:9px;color:#8ea7b5;padding:8px}
.subscribe i{width:28px;border-left:1px solid #6e8c9d;display:flex;align-items:center;justify-content:center}
.bottom-bar{height:41px;background:var(--blue);text-align:center;font-size:9.5px;color:var(--white);line-height:41px}
.bottom-bar b{font-weight:700}
</style>
</head>
<body>

<nav class="site-nav">
  <div class="brand"><span class="brand-dot"></span><span class="brand-name">Corvantis Portal</span></div>
  <div class="nav-links"><span class="active">HOME</span><span>ABOUT US</span><span>PROGRAMS</span><span>FAQ</span><span>CONTACT</span></div>
  <div class="nav-login">LOGIN</div>
</nav>

<header class="hero">
  <div class="photo hero-photo" role="img" aria-label="Eye doctor examining a patient at a slit lamp"></div>
  <div class="hero-shade"></div>
  <h1 class="hero-title">LEARN FASTER AND SMARTER</h1>
  <p class="hero-text">Corvantis Portal helps undergraduates and healthcare professionals learn or update their knowledge about the clinically relevant anatomy, pathology, examination techniques and common eye disorders of the human eye.</p>
  <div class="hero-actions">
    <span class="btn">Undergraduates | Learn more</span>
    <span class="btn">Healthcare professionals | Learn more</span>
  </div>
  <div class="hero-dots"><span class="on"></span><span></span><span></span></div>
</header>

<section class="trusted">
  <h2 class="spaced-title">Trusted across the world</h2>
  <div class="title-rule"></div>
  <div class="badges">
    <div class="badge"><span class="badge-shape"></span><span class="badge-bar"></span></div>
    <span class="badge-sep"></span>
    <div class="badge"><span class="badge-shape"></span><span class="badge-bar"></span></div>
    <span class="badge-sep"></span>
    <div class="badge"><span class="badge-shape"></span><span class="badge-bar"></span></div>
    <span class="badge-sep"></span>
    <div class="badge"><span class="badge-shape"></span><span class="badge-bar"></span></div>
  </div>
</section>

<section class="why">
  <h2 class="spaced-title">Why Corvantis Portal?</h2>
  <div class="title-rule"></div>

  <div class="frame" style="left:232px;top:178px;width:230px;height:290px"></div>
  <div class="photo" style="left:250px;top:196px;width:222px;height:278px;background:linear-gradient(135deg,#d9e4ea,#a9bcc7)" role="img" aria-label="Clinician performing an eye examination with a slit lamp"></div>
  <div class="abs" style="left:610px;top:280px;width:330px">
    <h3 class="feature-heading">Credible</h3>
    <p class="feature-copy">Written and reviewed by a team of consultant eye surgeons and teachers.</p>
    <ul class="feature-list">
      <li>Images and figures by experts</li>
      <li>Based on current clinical practice</li>
      <li>Endorsed by leading medical colleges</li>
    </ul>
  </div>

  <div class="abs" style="left:296px;top:620px;width:330px">
    <h3 class="feature-heading">Visual</h3>
    <p class="feature-copy">Every lesson uses clear 3D animations and diagrams.</p>
    <ul class="feature-list">
      <li>Step-by-step animated anatomy</li>
      <li>Common eye disorders explained visually</li>
      <li>Learn at your own pace, anywhere</li>
    </ul>
  </div>
  <div class="frame blue" style="left:650px;top:520px;width:290px;height:280px"></div>
  <div class="photo" style="left:666px;top:536px;width:276px;height:276px;background:linear-gradient(135deg,#f1efe9,#d7d3c8)" role="img" aria-label="Young girl covering one eye in front of an eye chart"></div>
</section>

<section class="modules">
  <div class="photo modules-bg" role="img" aria-label="Eye examination scene in blue tint"></div>
  <h2 class="spaced-title">Training modules</h2>
  <div class="title-rule"></div>

  <div class="module" style="left:180px">
    <div class="module-ring">
      <svg width="70" height="60" viewBox="0 0 70 60" fill="none" stroke="#fff" stroke-width="2.5"><polyline points="6,46 22,30 34,38 58,12"/><polyline points="48,12 58,12 58,22"/><line x1="4" y1="54" x2="66" y2="54"/></svg>
    </div>
    <div class="module-name">Core principles</div>
    <p class="module-text">Anatomy, physiology and optics of the eye in clear animated lessons.</p>
    <span class="btn">Learn more</span>
  </div>
  <div class="module" style="left:500px">
    <div class="module-ring">
      <svg width="64" height="64" viewBox="0 0 64 64" fill="none" stroke="#fff" stroke-width="2.5"><circle cx="32" cy="32" r="26"/><circle cx="32" cy="32" r="17"/><circle cx="32" cy="32" r="8"/><line x1="32" y1="32" x2="58" y2="8"/></svg>
    </div>
    <div class="module-name">Ophthalmology in practice</div>
    <p class="module-text">Examination, diagnosis and management of common eye conditions.</p>
    <span class="btn">Learn more</span>
  </div>
  <div class="module" style="left:820px">
    <div class="module-ring">
      <svg width="70" height="60" viewBox="0 0 70 60" fill="none" stroke="#fff" stroke-width="2.5"><circle cx="35" cy="14" r="8"/><path d="M23 36c0-8 24-8 24 0"/><circle cx="14" cy="32" r="6"/><circle cx="56" cy="32" r="6"/><path d="M4 52c0-7 20-7 20 0M46 52c0-7 20-7 20 0"/><line x1="35" y1="38" x2="35" y2="46"/></svg>
    </div>
    <div class="module-name">CPD & more</div>
    <p class="module-text">Quizzes, case studies and certificates for continuing learning.</p>
    <span class="btn">Learn more</span>
  </div>
</section>

<section class="team">
  <h2 class="spaced-title">Meet our team</h2>
  <div class="title-rule"></div>

  <div class="member" style="left:235px">
    <div class="member-photo" role="img" aria-label="Portrait of team member in a white coat"></div>
    <div class="member-bar"><div class="member-name">Dale Harrow</div><div class="member-role">Consultant ophthalmic surgeon</div></div>
  </div>
  <div class="member featured" style="left:485px">
    <div class="member-photo"></div>
    <div class="featured-inner">
      <div class="member-name">Ines Varga</div>
      <div class="member-role">Medical education lead</div>
      <p>Ines leads our teaching content, turning clinical knowledge into short animated lessons that are easy to follow and remember for students and staff.</p>
      <span class="btn">Learn more</span>
    </div>
  </div>
  <div class="member" style="left:735px">
    <div class="member-photo" role="img" aria-label="Portrait of team member in a white coat"></div>
    <div class="member-bar"><div class="member-name">Tomas Relling</div><div class="member-role">Lead 3D animator</div></div>
  </div>
</section>

<section class="testimonials">
  <h2 class="spaced-title">What are people saying about Corvantis Portal?</h2>
  <div class="title-rule"></div>
  <svg class="arrow" style="left:150px" width="24" height="14" viewBox="0 0 24 14" fill="none" stroke="#fff" stroke-width="2"><polyline points="8,1 2,7 8,13"/><line x1="2" y1="7" x2="23" y2="7"/></svg>
  <svg class="arrow" style="left:1026px" width="24" height="14" viewBox="0 0 24 14" fill="none" stroke="#fff" stroke-width="2"><polyline points="16,1 22,7 16,13"/><line x1="1" y1="7" x2="22" y2="7"/></svg>
  <div class="avatar" role="img" aria-label="Reviewer portrait"></div>
  <div class="quote-author">ALAN MERCER</div>
  <div class="quote-role">Eye Unit, City Hospital</div>
  <p class="quote-lead">Consultant ophthalmologist and head of the school of ophthalmology.</p>
  <p class="quote-body">When we introduced the portal to our trainees, understanding of eye anatomy improved within weeks. The animations make complex structures easy to picture, and the short modules fit well around clinical work. I recommend it to every student and nurse starting in ophthalmology.</p>
  <div class="t-dots"><span class="on"></span><span></span><span></span></div>
</section>

<section class="trial">
  <div class="photo trial-bg" role="img" aria-label="Patient having an eye examination, teal tint"></div>
  <div class="trial-circle" style="left:442px;background:linear-gradient(135deg,#f3e9e2,#d5c2b6)" role="img" aria-label="Eye examination photo"></div>
  <div class="trial-circle" style="left:525px;background:linear-gradient(135deg,#6d90a8,#2d5470);z-index:2" role="img" aria-label="Eye examination equipment photo"></div>
  <div class="trial-circle" style="left:608px;background:linear-gradient(135deg,#e8eef2,#b9c8d2)" role="img" aria-label="Eye examination photo"></div>
  <h2 class="trial-title">Want to try Corvantis Portal<br>for free?</h2>
  <p class="trial-note">No credit card details required. It's completely free for 7 days</p>
  <span class="btn">Start the trial</span>
</section>

<section class="charity">
  <h2>We give 10% of our profits to charity</h2>
  <p>We believe it is important to give something back so from 2016 we will donate 10% of every subscription to a selected charity somewhere in the world which works to help prevent sight loss and treat eye diseases.</p>
</section>

<section class="contact">
  <div class="photo contact-photo" role="img" aria-label="Smiling optometrist beside an eye examination machine"></div>
  <div class="contact-panel"></div>
  <div class="contact-kicker">GET IN TOUCH</div>
  <h2 class="contact-title">CONTACT</h2>
  <p class="contact-intro">Send us a message and our team will reply within one working day with the answers you need.</p>
  <div class="field" style="left:608px;top:222px;width:114px">Name</div>
  <div class="field" style="left:796px;top:222px;width:114px">Email</div>
  <div class="field" style="left:608px;top:266px;width:302px">Phone number</div>
  <div class="field focus" style="left:608px;top:310px;width:302px">Institution</div>
  <div class="field" style="left:608px;top:354px;width:302px;height:96px">Message</div>
  <span class="btn">Send message</span>
</section>

<footer class="site-footer">
  <div class="brand"><span class="brand-dot"></span><span class="brand-name">Corvantis Portal</span></div>
  <div class="community">COMMUNITY</div>
  <div class="socials"><span></span><span></span><span></span></div>
  <div class="foot-col" style="left:486px"><h4>COMPANY</h4><ul><li>About</li><li>Blog</li></ul></div>
  <div class="foot-col" style="left:640px"><h4>POLICIES</h4><ul><li>Terms of Use</li><li>Privacy and Cookies</li></ul></div>
  <div class="foot-col" style="left:794px"><h4>SUBSCRIBE</h4>
    <p>Join our mailing list for news, new lessons and special offers.</p>
    <div class="subscribe"><span>Your email here</span><i><svg width="12" height="12" viewBox="0 0 12 12" fill="none" stroke="#b9cad4" stroke-width="1.5"><polyline points="4,2 8,6 4,10"/></svg></i></div>
  </div>
</footer>
<div class="bottom-bar">© 2016 All rights reserved <b>Corvantis Portal</b></div>

</body>
</html>
```